Official personalized stationery with official coat of arms

I am looking for custom stationery design such as US letter size (8.5 X 11 or 21.6cm X 27.9cm), email signature (email) and envelope for US letter size (standard envelope no. 10 or 10.5cm X 24.5cm). Inspired by my personal coat of arms and my postal address:

4186 rue des Tilleuls
Levis, Quebec, H2K 4P7
Canada

Ideally a discreet design based on the coat of arms of Lucien Morvan but inspired by my mother's original coat of arms.

Something golden and translucent, simple but tasteful, without overemphasizing the green color. The coat of arms should have green, but not the entire structure of the stationery.

I am also looking for a small official thank you card in half letter size.

The design must be with the Lucien Morvan coat of arms and not the full coat of arms

Target Market(s)

For official communication

Industry/Entity Type

Communication officiel et parlementaire

Font styles to use
Other font styles liked:
• J’aime bien l’écriture comme le logo de la maison Delorme la police pour écrire le nom Delorme

Requirements
Must have
• Simplicity and use the Lucien Morvan coat of arms and not the full coat of arms
Nice to have
• Official and royal appearance as it is an official heraldic title of the British crown
Should not have
• Email and website

```html
<!DOCTYPE html>
<html lang="fr">
<head>
<meta charset="utf-8">
<title>Papeterie officielle — Armoiries Lucien Morvan</title>
<link href="https://fonts.googleapis.com/css2?family=Mulish:wght@400;600;700&display=swap" rel="stylesheet">
<style>
  :root {
    --green: #055d10;
    --gold: #bf9a37;
    --purple: #4b00a0;
    --paper: #ffffff;
    --edge: #d2d2d2;
    --stage: #6a4226;
    --label: #ffffff;
    --ink: #333333;
  }
  html, body { margin: 0; padding: 0; overflow: hidden; }
  body {
    width: 1200px; height: 861px; position: relative;
    background: var(--stage);
    font-family: "Mulish", Arial, sans-serif;
  }
  .shapes { position: absolute; left: 0; top: 0; width: 1200px; height: 861px; }
  .abs { position: absolute; margin: 0; white-space: nowrap; }
  .section-label { color: var(--label); font-size: 25px; font-weight: 400; transform: translateX(-50%); letter-spacing: 0.5px; }
  .crest-name {
    position: absolute; width: 53px; height: 64px;
    display: flex; flex-direction: column; align-items: center; justify-content: center; gap: 4px;
    color: var(--green); font-weight: 700; font-size: 10px;
  }
  .crest-name .mark { width: 10px; height: 10px; background: var(--green); }
  .brand-title { color: var(--green); font-weight: 400; }
  .address { color: var(--gold); line-height: 1.3; }
  .footer-line { color: #ffffff; font-size: 9.6px; line-height: 15px; }
  .flap-title { color: #f4f0e6; font-size: 18.5px; transform: translateX(-50%); letter-spacing: 0.3px; }
  .sig-brand { color: var(--gold); font-size: 14.5px; line-height: 17px; }
  .sig-name { color: var(--green); font-size: 12px; font-weight: 700; }
  .sig-name small { font-size: 8.5px; font-weight: 600; margin-left: 3px; }
  .sig-item { color: var(--ink); font-size: 10.5px; line-height: 12px; }
</style>
</head>
<body>

<svg class="shapes" viewBox="0 0 2268 1627" aria-hidden="true">
  <defs>
    <g id="wave">
      <path d="M0,-7 C8,133 123,183 263,181 C333,180 393,165 433,157 C393,170 333,190 263,192 C113,195 0,140 0,60 Z" fill="var(--purple)"/>
      <path d="M0,70 C40,165 150,190 273,188 C453,185 593,135 693,138 C793,141 873,180 919,250 L0,250 Z" fill="var(--gold)"/>
      <path d="M0,78 C40,176 150,199 273,197 C453,195 593,148 693,151 C793,154 866,192 916,250 L0,250 Z" fill="var(--paper)"/>
      <path d="M0,85 C40,185 150,210 273,207 C453,205 593,158 693,161 C793,164 863,200 912,250 L0,250 Z" fill="var(--green)"/>
    </g>
    <path id="flap" d="M0,0 L1025,0 C1017,34 1012,69 972,84 C942,99 562,169 542,174 C512,181 482,181 462,177 L92,104 C42,94 22,79 14,54 Z"/>
  </defs>

  <!-- letterhead sheet -->
  <rect x="107" y="208" width="919" height="1189" fill="var(--paper)" stroke="var(--edge)"/>
  <line x1="719" y1="255" x2="719" y2="317" stroke="var(--edge)" stroke-width="2"/>
  <use href="#wave" transform="translate(107,1147)"/>

  <!-- envelope backs -->
  <rect x="1138" y="141" width="1025" height="459" fill="var(--paper)" stroke="var(--edge)"/>
  <use href="#flap" fill="var(--green)" transform="translate(1138,141)"/>
  <rect x="1131" y="339" width="1027" height="459" fill="var(--paper)" stroke="var(--edge)"/>
  <use href="#flap" fill="var(--gold)" transform="translate(1131,339)"/>
  <rect x="1098" y="541" width="1027" height="459" fill="var(--paper)" stroke="var(--edge)"/>
  <use href="#flap" fill="var(--purple)" transform="translate(1098,541)"/>

  <!-- envelope front -->
  <rect x="1069" y="757" width="1027" height="460" fill="var(--paper)" stroke="var(--edge)"/>
  <use href="#wave" transform="translate(1069,967) scale(1.118,1)"/>

  <!-- email signature -->
  <rect x="1081" y="1257" width="879" height="213" fill="var(--paper)"/>
  <line x1="1499" y1="1287" x2="1499" y2="1442" stroke="var(--edge)" stroke-width="2"/>
  <g fill="none" stroke="var(--gold)" stroke-width="2.5">
    <circle cx="1549" cy="1339" r="9"/>
    <path d="M1545,1333 q-2,7 4,12 l3,-2"/>
    <rect x="1540" y="1369" width="18" height="12"/>
    <path d="M1540,1369 l9,7 l9,-7"/>
  </g>
  <path d="M1548,1424 C1541,1414 1539,1410 1539,1406 A9,9 0 0 1 1557,1406 C1557,1410 1555,1414 1548,1424 Z" fill="var(--gold)"/>
  <circle cx="1548" cy="1406" r="3" fill="var(--paper)"/>
</svg>

<!-- section labels -->
<p class="abs section-label" style="left:861px; top:29px;">Envelope</p>
<p class="abs section-label" style="left:310px; top:758px;">Letterhead</p>
<p class="abs section-label" style="left:809px; top:798px;">Email Signature</p>

<!-- letterhead -->
<div class="crest-name" style="left:68px; top:118px;"><span class="mark"></span><span>Morvan</span></div>
<p class="abs brand-title" style="left:387px; top:131px; font-size:12.4px;">Armoiries Lucien Morvan</p>
<p class="abs address" style="left:387px; top:149px; font-size:7.4px; line-height:10px;">4186 Rue Des Tilleuls, Levis, Quebec,<br>H2K 4P7 Canada</p>
<p class="abs footer-line" style="left:324px; top:703px;">Armoiries Brisées de Lucien Morvan<br>Fils De Hélène Garnier</p>

<!-- envelope flaps -->
<p class="abs flap-title" style="left:871px; top:110px;">Armoiries Lucien Morvan</p>
<p class="abs flap-title" style="left:866px; top:211px;">Armoiries Lucien Morvan</p>
<p class="abs flap-title" style="left:853px; top:319px;">Armoiries Lucien Morvan</p>

<!-- envelope front -->
<div class="crest-name" style="left:580px; top:411px;"><span class="mark"></span><span>Morvan</span></div>
<p class="abs brand-title" style="left:644px; top:420px; font-size:13.4px;">Armoiries Lucien Morvan</p>
<p class="abs address" style="left:644px; top:438px; font-size:10px; line-height:13.5px;">4186 Rue Des Tilleuls, Levis, Quebec,<br>H2K 4P7 Canada</p>
<p class="abs footer-line" style="left:870px; top:608px;">Armoiries Brisées de Lucien Morvan<br>Fils De Hélène Garnier</p>

<!-- email signature -->
<div class="crest-name" style="left:580px; top:681px;"><span class="mark"></span><span>Morvan</span></div>
<p class="abs sig-brand" style="left:641px; top:678px;">Armoiries<br>Lucien Morvan</p>
<p class="abs sig-name" style="left:814px; top:678px;">Julien Baril,<small>Managing Director</small></p>
<p class="abs sig-item" style="left:832px; top:702px;">418.555.0172</p>
<p class="abs sig-item" style="left:832px; top:721px;">lucienmorvan@exemple.ca</p>
<p class="abs sig-item" style="left:832px; top:739px;">4186 Rue Des Tilleuls, Levis, Quebec,<br>H2K 4P7 Canada</p>

</body>
</html>
```